Walter Hobbs PA Card Logo

Current logo attached. Its 25 year old logo I have used. Looking for a new fresh elegant professional look/design for a law firm that has high net worth clientele and is estate planning business law firm. Firm mis in Palm Beach Florida.
One sided card linen stock white will be used. Logo section name section. Logo should include nice elegant design using the letter "G" perhapa (I am not wed to current font of the G on current logo.) Be creative there with logo design. My initials are WH.......color scheme I figure 3 tone... Raised Gold Foil, Blue name of firm = Walter Hobbs, P.A. My practice focus is Family and Business Asset Protection. My name is Walter W. Hobbs, Esq. Practice specialties include Asset Protection trusts, Business Succession Planning, LLC law, Estate Planning, Medicaid Planning (Maybe put those topics in bullets in a section of card. Bottom of card can be reserved smaller print address phone website and email address. Address section is not as important as logo and topics of practice on front. I foresee address section can be in dark blue. MY name and Topics dark blue as well.
Target Market(s)
affluent; business owners executives; wealth 2-10 million net worth
Industry/Entity Type
business law and estate planning
Contact Information for Business Card
White thick linen one sided

```html
<!DOCTYPE html>
<html lang="en">
<head>
<meta charset="UTF-8">
<title>Walter Hobbs, P.A. – Business Card</title>
<link href="https://fonts.googleapis.com/css2?family=Cinzel:wght@500;600&family=Poppins:wght@400;500&display=swap" rel="stylesheet">
<style>
  :root {
    --navy: #132f50;
    --gold: #c8952f;
    --white: #ffffff;
    --stage: #3a3a3a;
    --rule-grey: #c9ced6;
  }
  * { margin: 0; padding: 0; box-sizing: border-box; }
  html, body { width: 1200px; height: 875px; overflow: hidden; background: var(--stage); }
  .canvas {
    width: 1200px; height: 875px;
    display: flex; flex-direction: column; align-items: center; justify-content: center; gap: 50px;
  }
  .card {
    position: relative; width: 640px; height: 366px; border-radius: 22px; overflow: hidden;
    box-shadow: 0 14px 30px rgba(0,0,0,.35);
  }
  .card--front { background: var(--navy); color: var(--white); }
  .card--back { background: var(--white); color: var(--navy); }

  .brand { position: absolute; display: flex; align-items: center; gap: 24px; }
  .brand__mark { width: 96px; height: 96px; flex: none; }
  .card--front .brand__mark { background: var(--white); }
  .card--back .brand__mark { background: var(--gold); }
  .brand__text { display: flex; flex-direction: column; align-items: center; }
  .brand__name {
    font-family: "Cinzel", serif; font-weight: 600; font-size: 37px; letter-spacing: 1.5px; line-height: 1;
    white-space: nowrap;
  }
  .brand__tagline {
    display: flex; align-items: center; gap: 12px; margin-top: 9px;
    font-family: "Cinzel", serif; font-weight: 500; font-size: 17px; letter-spacing: 3px; white-space: nowrap;
  }
  .brand__rule { width: 54px; height: 2px; background: currentColor; }
  .card--back .brand__rule { background: var(--gold); }

  .card--front .brand { left: 50%; top: 50%; transform: translate(-50%, -50%); }
  .card--back .brand { left: 50%; top: 48px; transform: translateX(-50%); }
  .card--back .brand__name { font-size: 35px; }

  .person { position: absolute; left: 52px; top: 212px; display: flex; flex-direction: column; align-items: flex-end; }
  .person__name { font-family: "Cinzel", serif; font-weight: 600; font-size: 25px; letter-spacing: 1px; white-space: nowrap; }
  .person__title { font-family: "Poppins", sans-serif; font-size: 12.5px; margin-top: 1px; white-space: nowrap; }

  .divider { position: absolute; left: 334px; top: 200px; width: 1px; height: 66px; background: var(--rule-grey); }

  .contact { position: absolute; left: 360px; top: 198px; list-style: none;
    font-family: "Poppins", sans-serif; font-size: 12.5px; line-height: 22px; }
  .contact li { display: flex; align-items: center; gap: 8px; white-space: nowrap; }
  .contact svg { width: 11px; height: 11px; fill: var(--navy); flex: none; }

  .address-band {
    position: absolute; left: 0; right: 0; bottom: 26px; height: 40px; background: var(--navy); color: var(--white);
    display: flex; align-items: center; justify-content: center;
    font-family: "Poppins", sans-serif; font-size: 13px; letter-spacing: .3px;
  }
</style>
</head>
<body>
<main class="canvas">

  <section class="card card--front" aria-label="Card front">
    <div class="brand">
      <div class="brand__mark"></div>
      <div class="brand__text">
        <span class="brand__name">Walter Hobbs, P.A.</span>
        <span class="brand__tagline"><span class="brand__rule"></span>Elder Law Attorney<span class="brand__rule"></span></span>
      </div>
    </div>
  </section>

  <section class="card card--back" aria-label="Card back">
    <div class="brand">
      <div class="brand__mark"></div>
      <div class="brand__text">
        <span class="brand__name">Walter Hobbs, P.A.</span>
        <span class="brand__tagline"><span class="brand__rule"></span>Elder Law Attorney<span class="brand__rule"></span></span>
      </div>
    </div>

    <div class="person">
      <p class="person__name">Walter W. Hobbs</p>
      <p class="person__title">Esq, Practice specialties</p>
    </div>

    <div class="divider"></div>

    <ul class="contact">
      <li><svg viewBox="0 0 12 12"><path d="M2.5 1h2l1 3-1.4 1a6 6 0 0 0 2.9 2.9l1-1.4 3 1v2A1.5 1.5 0 0 1 9.5 11 8.5 8.5 0 0 1 1 2.5 1.5 1.5 0 0 1 2.5 1z"/></svg>+1 561-555-0148</li>
      <li><svg viewBox="0 0 12 12"><path d="M1 2.5h10v7H1z"/><path d="M1.5 3l4.5 3.5L10.5 3" stroke="#fff" stroke-width="1" fill="none"/></svg>name@hobbsestatelaw.com</li>
      <li><svg viewBox="0 0 12 12"><circle cx="6" cy="6" r="5"/><path d="M1 6h10M6 1c-2 2.5-2 7.5 0 10M6 1c2 2.5 2 7.5 0 10" stroke="#fff" stroke-width=".8" fill="none"/></svg>www.hobbsestatelaw.com</li>
    </ul>

    <div class="address-band">2240 Harbor Point Ave., Lake Worth, Float 33460</div>
  </section>

</main>
</body>
</html>
```